Business card

We need a business card design for our company based in Auckland , New Zealand called 'Quill + Habitat Ltd'. We provide architectural services. We would like to see designs that use the max. three colours (such as white, black, grey) The final design should communicate financial safety and growth."
Also I will provide our company logo. I would like to the logo to be embeded onto our business card.

Target Market(s)

new residential house, alteration & addition & light commericila design & drafting service

Industry/Entity Type

Architecture

Contact Information for Business Card

Company name: quill + habitat Ltd.
Name: Rowan Teale
Job title: architectural designer & Design QWR
email address: rowan@qandh.co.nz
mobile number: 02 5136 2297
web site: www.qandh.co.nz

Requirements
Must have
• My project must have..
• - embeded logo (attached company logo)
• I don't have a bigger version for our company logo, but I have one old one, so you can remove the word from it)
• - insert the attached small GVTK logo & QWR logo
• - creative, simple and clear business card.
• - Max. three colours
Nice to have
• - Here are the samples I would like to share with you: http://www.velmoriq.com/blog/sparse-stationery-layouts/
• I would like to have my business card like one of the creation.
Should not have
• TBA

```html
<!DOCTYPE html>
<html lang="en">
<head>
<meta charset="utf-8">
<title>Quill + Habitat Ltd — Business Card</title>
<link rel="stylesheet" href="https://fonts.googleapis.com/css2?family=Roboto+Condensed:wght@300;400&display=swap">
<style>
  :root {
    --backdrop: #3b3b3b;
    --card-white: #ffffff;
    --card-dark: #404040;
    --accent: #f7941d;
    --ink: #2b2b2b;
    --faint: #e8e8e8;
    --badge: #2f2f2f;
    --badge-soft: #b9b9b9;
  }
  * { margin: 0; padding: 0; box-sizing: border-box; }
  html, body {
    width: 1200px; height: 1200px; overflow: hidden;
    background: var(--backdrop);
    font-family: "Roboto Condensed", "Arial Narrow", sans-serif;
  }
  .canvas { position: relative; width: 1200px; height: 1200px; }
  .card {
    position: absolute; left: 272px; width: 640px; height: 363px; overflow: hidden;
  }
  .card--front { top: 222px; background: var(--card-white); }
  .card--back { top: 645px; background: var(--card-dark); }

  .brand-watermark {
    position: absolute; right: 22px; top: 28px;
    font-size: 46px; font-weight: 300; color: var(--faint);
    letter-spacing: 1px; white-space: nowrap;
  }
  .accent-bar {
    position: absolute; left: 0; top: 181px; width: 12px; height: 52px;
    background: var(--accent);
  }
  .person-name {
    position: absolute; left: 26px; top: 178px;
    font-size: 31px; font-weight: 300; color: var(--accent); line-height: 1;
  }
  .person-title {
    position: absolute; left: 26px; top: 212px;
    font-size: 19px; font-weight: 300; color: var(--ink); line-height: 1;
  }
  .contact-list { position: absolute; left: 26px; top: 266px; list-style: none; }
  .contact-item {
    display: flex; align-items: center; height: 24px;
    font-size: 20px; font-weight: 300; color: var(--ink);
  }
  .contact-icon { width: 18px; height: 18px; margin-right: 17px; flex: none; }

  .badge-practitioner {
    position: absolute; left: 456px; top: 264px; width: 68px; height: 68px;
    border-radius: 50%; background: var(--badge);
  }
  .badge-association {
    position: absolute; left: 540px; top: 272px; width: 48px; height: 44px;
    background: var(--badge-soft);
  }

  .back-brand {
    position: absolute; left: 0; right: 0; top: 50%; transform: translateY(-50%);
    display: flex; align-items: center; justify-content: center; gap: 12px;
    color: var(--accent); font-size: 28px; font-weight: 300;
  }
  .back-brand__dot { width: 14px; height: 14px; border-radius: 50%; background: var(--accent); }
</style>
</head>
<body>
<main class="canvas">
  <section class="card card--front" aria-label="Business card front">
    <div class="brand-watermark">quill + habitat</div>
    <div class="accent-bar"></div>
    <h1 class="person-name">Rowan Teale</h1>
    <p class="person-title">architectural designer &amp; Design QWR</p>
    <ul class="contact-list">
      <li class="contact-item">
        <svg class="contact-icon" viewBox="0 0 18 18" aria-hidden="true">
          <rect x="1" y="4" width="16" height="11" fill="var(--accent)"/>
          <path d="M1 4 L9 10 L17 4" fill="none" stroke="#fff" stroke-width="1.4"/>
        </svg>
        rowan@qandh.co.nz
      </li>
      <li class="contact-item">
        <svg class="contact-icon" viewBox="0 0 18 18" aria-hidden="true">
          <rect x="4" y="1" width="10" height="16" rx="2" fill="none" stroke="var(--accent)" stroke-width="1.6"/>
          <line x1="7.5" y1="14.5" x2="10.5" y2="14.5" stroke="var(--accent)" stroke-width="1.4"/>
        </svg>
        02 5136 2297
      </li>
      <li class="contact-item">
        <svg class="contact-icon" viewBox="0 0 18 18" aria-hidden="true">
          <g fill="none" stroke="var(--accent)" stroke-width="1.3">
            <circle cx="9" cy="9" r="7.5"/>
            <ellipse cx="9" cy="9" rx="3.3" ry="7.5"/>
            <line x1="1.5" y1="9" x2="16.5" y2="9"/>
            <line x1="2.8" y1="5" x2="15.2" y2="5"/>
            <line x1="2.8" y1="13" x2="15.2" y2="13"/>
          </g>
        </svg>
        www.qandh.co.nz
      </li>
    </ul>
    <div class="badge-practitioner" role="img" aria-label="Licensed practitioner badge"></div>
    <div class="badge-association" role="img" aria-label="GVTK professional member badge"></div>
  </section>

  <section class="card card--back" aria-label="Business card back">
    <div class="back-brand">
      <span class="back-brand__dot"></span>
      <span class="back-brand__name">quill + habitat Ltd.</span>
    </div>
  </section>
</main>
</body>
</html>
```